Business Card Design

I am a Building Surveyor and run my own Building Consultat company, providing professional advice and services to builders, architects, designers, owners, etc.

Industry/Entity Type

Business

Contact Information for Business Card

Dorwen Halket BBldgSurv (Hons)
Managing Director

57 Quillon Rise, Marrick Heights WA 6148
Mobile 0438 271 594
Email Dorwen.halket@tarnwellpq.com

Requirements
Must have
• I would like the back of the business card to be one colour (a shade of either black or maroon, matching the colours of my logo). Positioned in the centre on the back of the business card is to be my logo.

The front of the card is to be white, with my contact information in either black or maroon. The ADBldgSurv after my name should be in a smaller font size than my name. I would also like a small logo somewhere on this side of the card.

```html
<!DOCTYPE html>
<html lang="en">
<head>
<meta charset="utf-8">
<title>Tarnwell Building Consultants – Business Card</title>
<link rel="stylesheet" href="https://fonts.googleapis.com/css2?family=Ubuntu:ital,wght@0,400;0,500;1,400&family=Arimo:ital,wght@0,400;1,400&display=swap">
<style>
  :root {
    --page: #ffffff;
    --card-white: #ffffff;
    --card-black: #0d0d0d;
    --frame-red: #d4191c;
    --ink: #111111;
    --maroon: #7a1517;
    --skyline-light: #efeee9;
    --skyline-dark: #171717;
    --mark-dark: #2b2b2b;
    --mark-maroon: #4a1012;
    --icon-grey: #dcdcdc;
  }
  * { margin: 0; padding: 0; box-sizing: border-box; }
  html, body { width: 960px; height: 1200px; overflow: hidden; background: var(--page); }
  .sheet { position: relative; width: 960px; height: 1200px; }

  .card-frame { position: absolute; border: 3px solid var(--frame-red); }
  .card-frame--front { left: 59px; top: 51px; width: 835px; height: 478px; background: var(--card-white); overflow: hidden; }
  .card-frame--back { left: 48px; top: 584px; width: 861px; height: 522px; background: var(--page); }

  .card-back { position: absolute; left: 14px; top: 13px; width: 826px; height: 501px; background: var(--card-black); overflow: hidden; }

  .skyline { position: absolute; }
  .skyline--front { left: 12px; top: 34px; width: 260px; height: 426px;
    background: linear-gradient(90deg, var(--skyline-light) 0%, #f4f3ef 55%, rgba(255,255,255,0) 100%); }
  .skyline--back { left: 0; top: 140px; width: 826px; height: 361px;
    background: linear-gradient(180deg, rgba(23,23,23,0) 0%, var(--skyline-dark) 30%, #141414 100%); }

  .brand { position: absolute; display: flex; align-items: center; font-family: "Ubuntu", sans-serif; font-weight: 500; }
  .brand__dot { border-radius: 50%; flex: none; }
  .brand__name { display: flex; flex-direction: column; align-items: center; line-height: 1; }

  .brand--front { left: 266px; top: 66px; color: var(--ink); }
  .brand--front .brand__dot { width: 92px; height: 92px; background: var(--maroon); margin-right: 18px; }
  .brand--front .brand__word { font-size: 52px; letter-spacing: 10px; }
  .brand--front .brand__tag { font-size: 16px; letter-spacing: 2px; margin-top: 6px; }

  .brand--back { left: 62px; top: 178px; color: var(--mark-dark); }
  .brand--back .brand__dot { width: 128px; height: 128px; background: var(--mark-maroon); margin-right: 30px; }
  .brand--back .brand__word { font-size: 72px; letter-spacing: 16px; }
  .brand--back .brand__tag { font-size: 24px; letter-spacing: 3px; margin-top: 10px; }

  .rule-bar { position: absolute; left: 277px; top: 166px; width: 544px; height: 19px; background: var(--ink); }
  .rule-line { position: absolute; left: 277px; top: 191px; width: 544px; height: 3px; background: var(--maroon); }

  .holder { position: absolute; left: 294px; top: 218px; }
  .holder__name { font-family: "Ubuntu", sans-serif; font-weight: 500; font-size: 29px; color: var(--ink); }
  .holder__role { font-family: "Arimo", sans-serif; font-style: italic; font-size: 18px; color: var(--ink); margin-top: 4px; }

  .contact { position: absolute; left: 416px; top: 318px; font-family: "Arimo", sans-serif; font-size: 19px; color: var(--ink); list-style: none; }
  .contact__item { display: flex; align-items: center; height: 42px; }
  .contact__icon { width: 30px; height: 30px; margin: 0 8px 0 4px; flex: none; }
</style>
</head>
<body>
<main class="sheet">
  <section class="card-frame card-frame--front" aria-label="Card front">
    <div class="skyline skyline--front" role="img" aria-label="Faint city skyline illustration"></div>

    <div class="brand brand--front">
      <span class="brand__dot"></span>
      <span class="brand__name">
        <span class="brand__word">TARNWELL</span>
        <span class="brand__tag">BUILDING CONSULTANTS</span>
      </span>
    </div>

    <div class="rule-bar"></div>
    <div class="rule-line"></div>

    <div class="holder">
      <p class="holder__name">Dorwen Halket</p>
      <p class="holder__role">ADBldgSurv Director</p>
    </div>

    <ul class="contact">
      <li class="contact__item">57 Quillon Rise, Marrick Heights WA 6148</li>
      <li class="contact__item">
        <svg class="contact__icon" viewBox="0 0 30 30" aria-hidden="true">
          <circle cx="15" cy="15" r="14" fill="var(--icon-grey)"/>
          <rect x="8" y="9" width="14" height="4" rx="2" fill="none" stroke="#555" stroke-width="1.5"/>
          <rect x="10" y="13" width="10" height="8" fill="none" stroke="#555" stroke-width="1.5"/>
          <circle cx="15" cy="17" r="2" fill="#555"/>
        </svg>
        0438.271.594
      </li>
      <li class="contact__item">
        <svg class="contact__icon" viewBox="0 0 30 30" aria-hidden="true">
          <circle cx="15" cy="15" r="14" fill="var(--icon-grey)"/>
          <rect x="8" y="10" width="14" height="10" fill="none" stroke="var(--maroon)" stroke-width="1.6"/>
          <path d="M8 10 L15 16 L22 10" fill="none" stroke="var(--maroon)" stroke-width="1.6"/>
        </svg>
        Dorwen.halket@tarnwellpq.com
      </li>
    </ul>
  </section>

  <section class="card-frame card-frame--back" aria-label="Card back">
    <div class="card-back">
      <div class="skyline skyline--back" role="img" aria-label="Faint dark city skyline illustration"></div>
      <div class="brand brand--back">
        <span class="brand__dot"></span>
        <span class="brand__name">
          <span class="brand__word">TARNWELL</span>
          <span class="brand__tag">BUILDING CONSULTANTS</span>
        </span>
      </div>
    </div>
  </section>
</main>
</body>
</html>
```